Local Motorsports Photography Business Card Design

Looking for a Logo and Business Card design for my father who is a local photographer based in Perth operating under the business name "KLR Photography". Specializing in Motorsports (Torque Racers/Hyperwheels/Corvan Trial) and events photography.
Would like it to look professional, while still maintaining a local/personal feel. Color\Design of the Logo and Card are open to your own interpretation, but should limit the color scheme to around 2-3 colors.
Design should be a logo one side and contact details on the rear. The website currently is very simple and a generic template and should not be used as a basis for design.
Industry/Entity Type
Business
Contact Information for Business Card
Name: Malcolm Purdie
Website: www.klrphotography-example.com.au
Email: malcolm@klrphotography-example.com.au
Phone: 0471 629 385
Look and feel
Each slider illustrates characteristics of the customer's brand and the style your logo design should communicate.

```html
<!DOCTYPE html>
<html lang="en">
<head>
<meta charset="utf-8">
<title>KLR Photography – Business Card</title>
<link href="https://fonts.googleapis.com/css2?family=Questrial&display=swap" rel="stylesheet">
<style>
  :root {
    --page-bg: #eceef1;
    --card-white: #ffffff;
    --navy: #1f3f7a;
    --navy-deep: #071a4a;
    --royal: #1d4fa3;
    --ink: #3a3f4a;
    --rule: #c9ccd2;
    --on-dark: #ffffff;
  }
  * { box-sizing: border-box; margin: 0; padding: 0; }
  html, body {
    width: 1200px; height: 913px; overflow: hidden;
    background: var(--page-bg);
    font-family: "Questrial", "Helvetica Neue", Arial, sans-serif;
  }
  .canvas {
    position: relative; width: 1200px; height: 913px;
    display: flex; align-items: center; justify-content: center; gap: 60px;
  }
  .card {
    width: 510px; height: 310px; border-radius: 4px;
    box-shadow: 0 10px 28px rgba(20, 30, 60, 0.18);
    position: relative; overflow: hidden;
  }
  .card--front { background: var(--card-white); display: flex; align-items: center; }
  .card--back {
    background: linear-gradient(160deg, var(--royal) 0%, var(--navy) 45%, var(--navy-deep) 100%);
    display: flex; align-items: center; justify-content: center;
  }
  .brand { display: flex; align-items: center; gap: 10px; }
  .brand__mark { width: 14px; height: 14px; background: var(--navy); }
  .brand__name { font-size: 24px; color: var(--navy); letter-spacing: 0.5px; white-space: nowrap; }
  .card--back .brand__mark { background: var(--on-dark); }
  .card--back .brand__name { color: var(--on-dark); font-size: 30px; }
  .front__logo { width: 245px; display: flex; justify-content: center; }
  .front__divider { width: 1px; height: 150px; background: var(--rule); }
  .front__details { padding-left: 28px; }
  .person { font-size: 21px; color: var(--royal); margin-bottom: 20px; }
  .contact { list-style: none; }
  .contact__item {
    display: flex; align-items: center; gap: 8px;
    font-size: 11.5px; color: var(--ink); line-height: 1.75;
  }
  .contact__icon { width: 11px; height: 11px; flex: none; fill: var(--navy); }
</style>
</head>
<body>
<main class="canvas">
  <section class="card card--front" aria-label="Business card front">
    <div class="front__logo">
      <div class="brand">
        <span class="brand__mark"></span>
        <span class="brand__name">KLR Photography</span>
      </div>
    </div>
    <div class="front__divider"></div>
    <div class="front__details">
      <h1 class="person">Malcolm Purdie</h1>
      <ul class="contact">
        <li class="contact__item">
          <svg class="contact__icon" viewBox="0 0 24 24"><path d="M6.6 10.8a15.1 15.1 0 0 0 6.6 6.6l2.2-2.2a1 1 0 0 1 1-.25 11.4 11.4 0 0 0 3.6.57 1 1 0 0 1 1 1V20a1 1 0 0 1-1 1A17 17 0 0 1 3 4a1 1 0 0 1 1-1h3.5a1 1 0 0 1 1 1c0 1.25.2 2.45.57 3.57a1 1 0 0 1-.25 1z"/></svg>
          0471 629 385
        </li>
        <li class="contact__item">
          <svg class="contact__icon" viewBox="0 0 24 24"><path d="M2 5h20v14H2z M2 5l10 8 10-8" /></svg>
          malcolm@klrphotography-example.com.au
        </li>
        <li class="contact__item">
          <svg class="contact__icon" viewBox="0 0 24 24"><circle cx="12" cy="12" r="10"/><path d="M2 12h20M12 2c3 3 3 17 0 20M12 2c-3 3-3 17 0 20" stroke="#fff" stroke-width="1.5" fill="none"/></svg>
          www.klrphotography-example.com.au
        </li>
      </ul>
    </div>
  </section>

  <section class="card card--back" aria-label="Business card back">
    <div class="brand">
      <span class="brand__mark"></span>
      <span class="brand__name">KLR Photography</span>
    </div>
  </section>
</main>
</body>
</html>
```